Bar Soap Packaging Design for Facial Cleansing Bar

Hi,

I have a business that sells soaps, lotions, and other skincare products and I'd like a design for a box for a bar soap that is primarily for women.

The name of the brand is 'Velmo Shea Blend' and the brand is all about renewal and rejuvenation.

I've attached my logo and photos of packaging for bar soaps that are best sellers in my market.

The box is 3 inches x 2 inches and has a white background.

Info to go on the box:

1. Brand name: Velmo Shea Blend

2. [To go below brand name]: Facial Bar

3. Address: Distributed by Haverlin Trading Ltd, 47 Marlow St., Kingston, Jamaica W.I.

4. Contact: tamsin@velmosheablend.example

5. Net Weight: 3.6 oz /102g

6. Ingredients: glycerine, palmitic acid, sodium chloride, water, cocoa butter, fragrance, AOS, EDTA, vitamin E, color.

7. Directions: Wet face. Lather soap in hands. Gently massage lather onto face and neck. Rinse with water and pat dry with a towel. For day, follow with a sunscreen. At night, follow with a serum and/or moisturizer.

8. Please put a circle somewhere on the front with the words: 'Boosts Hydration 100%' in the circle

9. Batch Code: [please leave space beside 'Batch Code' blank]

10. Best Before: April 2019

11. Please put somewhere on the the front: For Younger Looking Skin

12. Please put somewhere on the front: with Real Cocoa Butter and Vitamin E

Thank you,
Tamsin

Target Market(s)

Women 27 to 60 who are looking for anti-age skincare products that'll make them look younger

Industry/Entity Type

Business

Font styles to use
Sans Serif

Colors

Designer to choose colors to be used in the design.

Requirements
Must have
• The info that I've asked for in the brief
Nice to have
• A design similar to the packaging for the brand of soap 'Odra' that I've attached.
Should not have
• Not sure...

```html
<!DOCTYPE html>
<html lang="en">
<head>
<meta charset="utf-8">
<title>Velmo Shea Blend – Facial Bar Box</title>
<link rel="stylesheet" href="https://fonts.googleapis.com/css2?family=Open+Sans:ital,wght@0,400;0,600;0,700;1,400;1,700&family=Dancing+Script:wght@500&display=swap">
<style>
  :root {
    --stage: #e8e8ea;
    --white: #ffffff;
    --brand-purple: #4a2a8c;
    --cocoa-brown: #5a4636;
    --sky-light: #d6eef6;
    --sky-mid: #9fd4e6;
    --sky-deep: #5fb7d6;
    --navy: #1f4f9a;
    --ink-blue: #2a4f7a;
    --splash: #cfe6f2;
    --pod: #8a6a52;
  }
  * { box-sizing: border-box; margin: 0; padding: 0; }
  html, body { width: 1200px; height: 1200px; overflow: hidden; }
  body {
    background: var(--stage);
    font-family: "Open Sans", Arial, sans-serif;
    position: relative;
  }
  .panel { position: absolute; left: 150px; width: 900px; box-shadow: 0 6px 24px rgba(0,0,0,.12); overflow: hidden; }

  /* Front */
  .front-panel { top: 50px; height: 560px; background: var(--white); }
  .front-panel .wave { position: absolute; left: 0; top: 0; width: 900px; height: 560px; }
  .hero-art {
    position: absolute; left: 70px; top: 130px;
    width: 280px; height: 290px; border-radius: 46%;
    background: radial-gradient(ellipse at 38% 36%, var(--pod) 0 24%, var(--splash) 52%, rgba(207,230,242,0) 72%);
  }
  .brand-name {
    position: absolute; left: 395px; top: 30px;
    font-size: 128px; font-weight: 600; color: var(--brand-purple);
    line-height: 1; letter-spacing: -1px;
  }
  .variant {
    position: absolute; left: 400px; top: 180px;
    font-size: 38px; font-weight: 700; color: var(--cocoa-brown); letter-spacing: 1px;
  }
  .product-type {
    position: absolute; left: 400px; top: 226px;
    font-size: 54px; font-weight: 400; color: var(--cocoa-brown);
  }
  .hydration-badge {
    position: absolute; left: 725px; top: 140px;
    width: 130px; height: 130px; border-radius: 50%;
    background: var(--navy); border: 4px solid var(--white);
    box-shadow: 0 0 0 3px var(--sky-deep);
    color: var(--white); text-align: center;
    display: flex; flex-direction: column; justify-content: center;
  }
  .hydration-badge .pct { font-size: 30px; font-weight: 700; line-height: 1.1; }
  .hydration-badge .words { font-size: 16px; line-height: 1.2; }
  .tagline {
    position: absolute; left: 470px; top: 415px;
    font-family: "Dancing Script", cursive; font-size: 36px; color: var(--ink-blue);
  }
  .claim {
    position: absolute; left: 480px; top: 468px;
    font-size: 20px; font-weight: 700; color: var(--ink-blue);
  }

  /* Long side */
  .side-panel {
    top: 640px; height: 230px;
    background: linear-gradient(90deg, var(--sky-mid), var(--sky-light) 55%, var(--sky-mid));
    padding: 30px 48px; color: var(--ink-blue);
  }
  .side-panel p { font-size: 19px; line-height: 1.5; font-style: italic; margin-bottom: 14px; }
  .side-panel strong { font-weight: 700; }

  /* End flap */
  .end-panel {
    top: 900px; height: 250px; background: var(--white);
    display: flex; color: var(--ink-blue);
  }
  .end-panel .end-band { width: 24px; background: linear-gradient(180deg, var(--sky-deep), var(--sky-mid)); }
  .end-brand { width: 300px; padding: 40px 0 0 36px; }
  .end-brand .name { font-size: 64px; font-weight: 600; color: var(--brand-purple); line-height: 1; }
  .end-brand .sub { font-size: 20px; font-weight: 700; color: var(--cocoa-brown); margin-top: 10px; letter-spacing: 1px; }
  .end-brand .type { font-size: 26px; color: var(--cocoa-brown); }
  .end-info { flex: 1; padding: 34px 40px 0 10px; font-size: 17px; line-height: 1.55; }
  .end-info .weight { font-weight: 700; font-size: 20px; margin-bottom: 8px; }
  .end-info .codes { display: flex; gap: 40px; margin-top: 10px; }
  .end-info .blank { display: inline-block; width: 110px; border-bottom: 1px solid var(--ink-blue); height: 18px; vertical-align: bottom; }
</style>
</head>
<body>
  <section class="panel front-panel">
    <svg class="wave" viewBox="0 0 900 560" aria-hidden="true">
      <defs>
        <linearGradient id="bandFill" x1="0" y1="0" x2="1" y2="1">
          <stop offset="0" stop-color="#9fd4e6"/>
          <stop offset=".5" stop-color="#d6eef6"/>
          <stop offset="1" stop-color="#7cc4de"/>
        </linearGradient>
      </defs>
      <path d="M0 560 L0 520 C250 470 520 380 900 290 L900 560 Z" fill="url(#bandFill)"/>
      <path d="M0 520 C250 470 520 380 900 290" fill="none" stroke="#5fb7d6" stroke-width="6"/>
      <path d="M0 545 C260 495 540 405 900 318" fill="none" stroke="#ffffff" stroke-width="3" opacity=".7"/>
    </svg>
    <div class="hero-art" role="img" aria-label="Cocoa pods with green leaves and a splash of clear water"></div>
    <div class="brand-name">Velmo</div>
    <div class="variant">SHEA BLEND</div>
    <div class="product-type">Facial Bar</div>
    <div class="hydration-badge">
      <span class="pct">100%</span>
      <span class="words">Boosts<br>Hydration</span>
    </div>
    <div class="tagline">For Younger Looking Skin</div>
    <div class="claim">with Real Cocoa Butter and Vitamin E</div>
  </section>

  <section class="panel side-panel">
    <p><strong>Ingredients:</strong> glycerine, palmitic acid, sodium chloride, water, cocoa butter, fragrance, AOS, EDTA, vitamin E, color.</p>
    <p><strong>Directions:</strong> Wet face. Lather soap in hands. Gently massage lather onto face and neck. Rinse with water and pat dry with a towel. For day, follow with a sunscreen. At night, follow with a serum and/or moisturizer.</p>
  </section>

  <section class="panel end-panel">
    <div class="end-band"></div>
    <div class="end-brand">
      <div class="name">Velmo</div>
      <div class="sub">SHEA BLEND</div>
      <div class="type">Facial Bar</div>
    </div>
    <div class="end-info">
      <div class="weight">Net Weight: 3.6 oz / 102g</div>
      <div>Distributed by Haverlin Trading Ltd,<br>47 Marlow St., Kingston, Jamaica W.I.</div>
      <div>tamsin@velmosheablend.example</div>
      <div class="codes">
        <span>Batch Code: <span class="blank"></span></span>
        <span>Best Before: April 2019</span>
      </div>
    </div>
  </section>
</body>
</html>
```